Why engage Insight Harbor?

We are starting a new company that will perform usability consulting and offer usability lab rental. We are in need a one page description flyer.
Updates

Wow! We saw some very interesting and creative flyers posted for review in our contest.

Unfortunately, my schedule became a bit crazy and I may not get back to evaluating them until next week :(  In the meantime, I did want to say thank you for your entries!

Cheers!
Marla

Target Market(s)

product designers, human factors/usability researchers, consumer researcher firms, etc

Industry/Entity Type

It Company

Requirements
Must have
• We would like to see designs with a simple, yet modern, sophisticated feel. I will include our logo images that need to be incorporated along with the font used.

The file called flyer.pdf has all of the information that needs to be included.

Please include 1-3 appropriate stock photos. Please see text in flyer.pdf for description of our services.

Nice to have
• Additionally, there is a sample flyer design that we like for reference. Not a requirement...it is just a reference for the kind of style that we are looking for.

```html
<!DOCTYPE html>
<html lang="en">
<head>
<meta charset="utf-8">
<title>Insight Harbor – Usability Research Flyer</title>
<link rel="stylesheet" href="https://fonts.googleapis.com/css2?family=Open+Sans:wght@400;700&family=Bodoni+Moda:wght@700;800&display=swap">
<style>
  :root {
    --navy: #1c2f8c;
    --heading-blue: #1a3f9e;
    --lime: #8dc63f;
    --lime-panel: #a7d22b;
    --orange: #f47a20;
    --body-grey: #5a5a5a;
    --white: #ffffff;
    --chalk-dark: #2b2b2b;
    --chalk-mid: #4a4a48;
  }
  * { box-sizing: border-box; margin: 0; padding: 0; }
  html, body { width: 928px; height: 1200px; overflow: hidden; background: var(--white); }
  .flyer {
    position: relative; width: 928px; height: 1200px; overflow: hidden;
    background: var(--white); font-family: "Open Sans", Arial, sans-serif; color: var(--body-grey);
  }
  .tab {
    position: absolute; left: 186px; width: 264px; height: 26px; background: var(--orange);
  }
  .tab--top { top: 0; border-radius: 0 0 14px 14px; }
  .tab--bottom { bottom: 0; border-radius: 14px 14px 0 0; }

  .brand {
    position: absolute; left: 54px; top: 104px; width: 530px;
    display: flex; align-items: center; gap: 14px;
  }
  .brand__mark { flex: none; width: 42px; height: 42px; border-radius: 50%; background: var(--orange); }
  .brand__name {
    font-family: "Open Sans", Arial, sans-serif; font-weight: 400; font-size: 50px;
    letter-spacing: 0; color: var(--navy); line-height: 1; white-space: nowrap;
  }

  .intro {
    position: absolute; left: 54px; top: 196px; width: 530px;
    font-size: 14px; line-height: 16.5px;
  }
  .intro p + p { text-indent: 6px; }

  .why-heading {
    position: absolute; left: 54px; top: 318px;
    font-family: "Bodoni Moda", "Times New Roman", serif; font-weight: 800;
    font-size: 30px; color: var(--heading-blue); letter-spacing: -0.3px;
  }

  .reason { position: absolute; left: 64px; width: 520px; display: flex; }
  .reason__num {
    flex: none; width: 40px; height: 40px; margin-top: 16px; border-radius: 50%;
    background: var(--lime); color: var(--white);
    font-family: "Bodoni Moda", "Times New Roman", serif; font-weight: 700; font-size: 26px;
    display: flex; align-items: center; justify-content: center; line-height: 1;
  }
  .reason__body { margin-left: 23px; font-size: 13px; line-height: 15px; }
  .reason__title { color: var(--lime); font-weight: 700; font-size: 13px; }

  .photo { position: absolute; }
  .photo--team {
    left: 54px; top: 1008px; width: 528px; height: 138px;
    background: linear-gradient(180deg, #e9eef2 0%, #c9d2da 45%, #3a3f4a 100%);
  }
  .photo--chalkboard {
    left: 614px; top: 0; width: 314px; height: 727px;
    background: linear-gradient(160deg, var(--chalk-mid) 0%, var(--chalk-dark) 60%, #1c1c1c 100%);
  }
  .photo--meeting {
    left: 614px; top: 982px; width: 314px; height: 218px;
    background: linear-gradient(180deg, #dfe7ee 0%, #c7d3dd 50%, #eef1f3 100%);
  }

  .contact-panel {
    position: absolute; left: 614px; top: 727px; width: 314px; height: 247px;
    background: var(--lime-panel); color: var(--white); padding: 90px 0 0 27px;
  }
  .contact-panel__name { font-weight: 700; font-size: 22px; line-height: 26px; }
  .contact-panel__line { font-weight: 700; font-size: 11.5px; line-height: 18px; white-space: nowrap; }
</style>
</head>
<body>
<main class="flyer">
  <div class="tab tab--top"></div>

  <header class="brand">
    <span class="brand__mark"></span>
    <span class="brand__name">INSIGHT HARBOR</span>
  </header>

  <section class="intro">
    <p>We are a network of human factors engineers, usability specialists, and cognitive/ consumer psychologists, who help you design and evaluate the usefulness, usability and desirability of your products.</p>
    <p>Lease our state of the art consumer research and usability lab, or partner with us on usability testing, eyetracking studies, participatory design, online survey research, ethnographic studies, focus groups and more.</p>
  </section>

  <h1 class="why-heading">Why Engage Insight Harbor?</h1>

  <article class="reason" style="top:371px">
    <span class="reason__num">1</span>
    <div class="reason__body">
      <h2 class="reason__title">Experience &amp; Service</h2>
      <p>Founded by a Professor of Cognitive Psychology and Human Factors with over twenty years of experience, our group includes MS and PhD level consultants with experience working for and consulting with companies like Northwind Labs, Alder Systems, Corvale Medical, Vantis Health, Meridian Hospitals, Hollis and Reed, Brightline, and Starfield Studios. Full range of consumer research and usability services, including ethnography, participatory design, questionnaires, user diaries, usability testing, usability evaluation, card sorting, psychometric scaling, focus groups and more.</p>
    </div>
  </article>

  <article class="reason" style="top:537px">
    <span class="reason__num">2</span>
    <div class="reason__body">
      <h2 class="reason__title">Range and Dedicated Client Service</h2>
      <p>Our consultants have extensive experience in design and evaluation of computing, web, tablet, smart phone, product, medical, consumer, and many other types of products and user interfaces. Client Service Specialist Need copies, printing, lunch, or dinner reservations? Our client service specialist will make sure you have everything you need.</p>
    </div>
  </article>

  <article class="reason" style="top:655px">
    <span class="reason__num">3</span>
    <div class="reason__body">
      <h2 class="reason__title">Onsite and Streaming Video/Editing</h2>
      <p>Sessions can be viewed in many ways: Through our observation mirror, in our meeting room via pan-tilt-zoom camera, at your site on your computer, on your tablet or phone. On-site video editing. Highlight video included in facility rental.</p>
    </div>
  </article>

  <article class="reason" style="top:759px">
    <span class="reason__num">4</span>
    <div class="reason__body">
      <h2 class="reason__title">Recruiting</h2>
      <p>Sizable database with ability to recruit research participants according to age, sex, occupation, health status, and other parameters.</p>
    </div>
  </article>

  <article class="reason" style="top:841px">
    <span class="reason__num">5</span>
    <div class="reason__body">
      <h2 class="reason__title">Office Space and Accessibility</h2>
      <p>Meeting room for work, phone calls and conference calls. Wireless Internet. Located on the first floor, with ample, free, convenient and handicap parking. Adjustable artificial and natural lighting.</p>
    </div>
  </article>

  <article class="reason" style="top:923px">
    <span class="reason__num">6</span>
    <div class="reason__body">
      <h2 class="reason__title">Transcription and Translation Services</h2>
      <p>Transcription services and word frequency key-words-in-context, and word co-occurrence analyses available. Several consultants fluent in both English and Spanish.</p>
    </div>
  </article>

  <div class="photo photo--team" role="img" aria-label="Photo of a diverse team of six business professionals standing in a row"></div>
  <div class="photo photo--chalkboard" role="img" aria-label="Photo of a man in shirt and tie thinking in front of a chalkboard covered in equations and diagrams"></div>

  <aside class="contact-panel">
    <p class="contact-panel__name">Insight Harbor</p>
    <p class="contact-panel__line">2140 W. Harbor View Road, Lakeport CA 95453</p>
    <p class="contact-panel__line">555.214.3870</p>
    <p class="contact-panel__line">www.insight-harbor.com</p>
  </aside>

  <div class="photo photo--meeting" role="img" aria-label="Photo of three colleagues smiling around a table reviewing documents"></div>

  <div class="tab tab--bottom"></div>
</main>
</body>
</html>
```